Copperfen Hollow Wine And Spirits

We need to design a website for our Liquor Store

Industry/Entity Type

Store

Number of Pages Required

4 page

Requirements
Must have
• Beer, Liquor, Wine & Cigar related theme.
• Mention our 8-locations addresses & maps info
Nice to have
• category for Beer, Liquor & Wine to setup database for item list to link our sql server database.

```html
<!DOCTYPE html>
<html lang="en">
<head>
<meta charset="utf-8">
<title>Copperfen Hollow Wine And Spirits</title>
<link rel="stylesheet" href="https://fonts.googleapis.com/css2?family=Mulish:wght@400;600;700;800&display=swap">
<style>
:root{
  --navy:#1f3c88;
  --gold:#e8a31a;
  --green:#2fa83a;
  --blue:#1f74c0;
  --red:#e2493b;
  --ink:#333;
  --muted:#777;
  --line:#e2e2e2;
  --page:#f4f4f4;
  --dark:#2a2a2a;
}
*{box-sizing:border-box;margin:0;padding:0}
html,body{width:1200px;height:4027px;overflow:hidden}
body{font-family:"Mulish",sans-serif;color:var(--ink);background:var(--page);font-size:14px}
.canvas{position:relative;width:1200px;height:4027px;overflow:hidden}
.abs{position:absolute}
.btn{display:inline-flex;align-items:center;justify-content:center;border-radius:20px;font-weight:700;font-size:12px;height:30px;padding:0 20px}
.btn-outline{border:2px solid var(--navy);color:var(--navy);background:#fff}
.btn-solid{background:var(--navy);color:#fff;border:2px solid var(--navy)}
.eyebrow{font-size:14px;color:var(--ink)}
.title{font-size:24px;font-weight:700;color:var(--gold)}

/* top bar */
.topbar{top:0;left:0;width:1200px;height:32px;background:#ececec;font-size:11px;color:#555;display:flex;align-items:center;justify-content:space-between;padding:0 156px}
.topbar .right{display:flex;align-items:center;gap:8px}
.dot{width:14px;height:14px;border-radius:50%;background:#555;display:inline-block}
/* header */
.header{top:32px;left:0;width:1200px;height:83px;background:#fff;display:flex;align-items:center;padding:0 156px}
.logo{display:flex;align-items:center;gap:10px;font-weight:800;font-size:21px;color:var(--navy);width:309px}
.logo .mark{width:22px;height:22px;border-radius:50%;background:var(--gold)}
.nav{display:flex;gap:34px;font-size:13px;color:#555;align-items:center}
.nav .active{color:var(--navy);font-weight:700;border-bottom:2px solid var(--navy);padding-bottom:4px}
.cart{margin-left:auto;display:flex;align-items:center;gap:10px;font-size:12px}
.cart .ico{width:30px;height:30px;border-radius:50%;background:var(--navy);display:flex;align-items:center;justify-content:center}
.cart b{display:block;color:var(--navy)}
/* hero */
.hero{top:115px;left:0;width:1200px;height:513px;background:radial-gradient(ellipse at 75% 40%,#7a2418 0%,#4a1410 45%,#200806 100%)}
.hero .kicker{left:234px;top:160px;color:var(--gold);font-size:20px;font-weight:600}
.hero h1{left:232px;top:190px;color:#fff;font-size:46px;font-weight:800}
.hero p{left:234px;top:262px;width:520px;color:#eee;font-size:15px;line-height:1.5}
.hero .btn{left:231px;top:320px}
.arrow{width:30px;height:50px;display:flex;align-items:center;justify-content:center}
/* category tiles */
.tile{top:652px;width:282px;height:162px;overflow:hidden}
.tile .bg{position:absolute;inset:0}
.tile .txt{position:absolute;right:16px;top:34px;text-align:right}
.tile .txt b{display:block;color:var(--gold);font-size:19px}
.tile .txt span{color:#fff;font-size:14px;font-weight:700}
.tile .tag{position:absolute;right:0;bottom:0;height:30px;width:110px;color:#fff;font-size:12px;font-weight:700;display:flex;align-items:center;justify-content:center;clip-path:polygon(14% 0,100% 0,100% 100%,0 100%)}
/* welcome */
.welcome-photo{top:875px;left:156px;width:456px;height:400px;background:linear-gradient(135deg,#c9a583,#7a5134 60%,#3e2818)}
.welcome{top:945px;left:663px;width:382px}
.welcome h2{font-size:24px;color:var(--gold);font-weight:700;margin:2px 0 18px}
.welcome p{font-size:12px;line-height:1.75;color:var(--muted);margin-bottom:16px}
/* products */
.products-head{top:1338px;left:156px;width:889px;display:flex;justify-content:space-between;align-items:flex-end}
.tabs{display:flex;gap:26px;align-items:center;font-size:13px;color:#555}
.tabs .on{color:var(--navy);font-weight:700;border-bottom:2px solid var(--navy)}
.card{top:1410px;width:201px;height:354px;background:#fff;text-align:center}
.card.raised{box-shadow:0 6px 18px rgba(0,0,0,.18)}
.card .shot{height:190px;margin:12px;background:linear-gradient(180deg,#fafafa,#e6e6e6)}
.card .badge{position:absolute;left:12px;top:0;color:#fff;font-size:11px;font-weight:700;padding:3px 10px}
.card h3{font-size:13px;font-weight:600;line-height:1.4;color:#444;margin-top:14px}
.card .price{font-size:22px;font-weight:800;color:var(--green);margin:12px 0 14px}
/* promos */
.promo{top:1818px;width:282px;height:161px;background:linear-gradient(120deg,#4b4b4b,#2a2a2a);color:#fff}
.promo .icon{position:absolute;left:18px;top:48px;width:60px;height:60px;display:flex;align-items:center;justify-content:center}
.promo .txt{position:absolute;right:18px;top:36px;text-align:right;font-size:15px;font-weight:700;line-height:1.25}
.promo .txt b{color:var(--gold)}
.promo .tag{position:absolute;right:0;bottom:0;height:30px;width:110px;background:var(--green);font-size:12px;font-weight:700;display:flex;align-items:center;justify-content:center;clip-path:polygon(14% 0,100% 0,100% 100%,0 100%)}
/* reviews */
.rev-title{top:2040px;font-size:22px;font-weight:700;color:var(--gold)}
.rev{top:2094px;width:433px;height:156px;color:#fff;padding:26px 26px 0 80px;font-size:14px;line-height:1.5}
.rev .q{position:absolute;left:26px;top:12px;font-size:56px;font-weight:800;line-height:1}
.rev .stars{color:#ffd23f;letter-spacing:1px}
.rev::after{content:"";position:absolute;left:30px;bottom:-18px;border:18px solid transparent;border-top-color:inherit;border-bottom:0;border-left-width:0}
.author{top:2280px;width:433px;display:flex;align-items:center;gap:14px}
.author .av{width:48px;height:48px;border-radius:50%;background:#9a9a9a}
.author b{font-size:13px;font-weight:700}
.author small{display:block;font-size:11px;color:var(--muted)}
.pager{margin-left:auto;display:flex;gap:8px}
.pager i{width:22px;height:22px;border-radius:50%;background:var(--green);display:flex;align-items:center;justify-content:center}
/* event */
.event{top:2398px;left:156px;width:889px;height:198px;background:linear-gradient(90deg,#151515 0%,#222 45%,#5a3a1c 80%,#2e1d0d 100%)}
.event h2{position:absolute;left:75px;top:44px;color:var(--green);font-size:32px;font-weight:600}
.event p{position:absolute;left:75px;top:86px;color:#fff;font-size:24px;font-weight:800}
.event .btn{position:absolute;left:75px;top:130px;border:2px solid #fff;color:#fff}
/* news */
.news-head{top:2660px;left:156px;width:889px}
.news{top:2733px;width:433px;height:161px;background:#fff;display:flex}
.news .shot{width:177px;height:161px}
.news .body{padding:24px 28px;font-size:13px;line-height:1.5;color:#555}
.news .date{color:var(--green);font-size:13px;margin-bottom:6px}
/* newsletter */
.newsletter{top:3023px;left:0;width:1200px;height:239px;background:linear-gradient(90deg,#3a2a18,#1e1610 30%,#1a1510 70%,#3a2a18);text-align:center}
.newsletter .eyebrow{color:#fff;margin-top:66px}
.newsletter .title{margin-top:2px}
.subscribe{display:flex;width:432px;margin:18px auto 0}
.subscribe span{flex:1;height:32px;background:#fff;font-size:11px;color:#888;text-align:left;padding:9px 12px}
.subscribe b{width:107px;height:32px;background:var(--green);color:#fff;font-size:12px;display:flex;align-items:center;justify-content:center}
/* contact */
.contact{top:3324px;left:156px;width:889px;height:140px;display:flex}
.contact .col{flex:1;text-align:center;border-right:1px solid var(--line);padding-top:18px}
.contact .col:last-child{border-right:0}
.contact h4{font-size:13px;font-weight:600;margin-top:10px}
.contact .val{font-size:13px;color:var(--navy);margin-top:4px}
.contact .phone{font-size:18px;font-weight:700}
/* map */
.map{top:3531px;left:0;width:1200px;height:429px;background:linear-gradient(135deg,#ece8df,#e3e1d8 50%,#d9e4d2)}
.pop{top:3678px;left:459px;width:212px;height:117px;background:#fff;box-shadow:0 2px 8px rgba(0,0,0,.25);text-align:center;font-size:12px;padding:12px 10px;line-height:1.45;color:#555}
.pop b{color:var(--ink)}
.pop .tel{color:var(--navy);font-weight:700;font-size:15px}
/* footer */
.footer{top:3960px;left:0;width:1200px;height:67px;background:var(--dark);color:#ccc;font-size:12px;display:flex;align-items:center;justify-content:space-between;padding:0 156px}
.footer .social{display:flex;gap:8px;align-items:center}
.footer .dot{background:#777}
</style>
</head>
<body>
<div class="canvas">

  <div class="abs topbar">
    <span>Extra 20%-40% Off Clearance</span>
    <div class="right"><span>Welcome User | Login | Register</span><i class="dot"></i><i class="dot"></i><i class="dot"></i><i class="dot"></i></div>
  </div>

  <header class="abs header">
    <div class="logo"><span class="mark"></span>Copperfen Hollow</div>
    <nav class="nav">
      <span class="active">Home</span><span>About</span><span>Products</span><span>News</span><span>Contact Us</span>
      <svg width="14" height="14" viewBox="0 0 14 14"><circle cx="6" cy="6" r="4.5" fill="none" stroke="#555" stroke-width="1.6"/><line x1="9.5" y1="9.5" x2="13" y2="13" stroke="#555" stroke-width="1.6"/></svg>
    </nav>
    <div class="cart">
      <span class="ico"><svg width="16" height="14" viewBox="0 0 16 14"><path d="M1 1h3l2 8h8l1.5-6H5" fill="none" stroke="#fff" stroke-width="1.5"/><circle cx="7" cy="12" r="1.3" fill="#fff"/><circle cx="13" cy="12" r="1.3" fill="#fff"/></svg></span>
      <div>Shopping Cart<b>Item(s) 00 - $0.00</b></div>
    </div>
  </header>

  <section class="abs hero" role="img" aria-label="Wine bottles on a warm dark red background">
    <div class="abs kicker">Buy Your</div>
    <h1 class="abs">Perfect Wine</h1>
    <p class="abs">There are many variations of passages of Lorem Ipsum available, but the majority have suffered...</p>
    <span class="abs btn btn-solid">Shop Now!</span>
    <div class="abs arrow" style="left:152px;top:208px"><svg width="16" height="32" viewBox="0 0 16 32"><path d="M14 2 2 16l12 14" fill="none" stroke="#fff" stroke-width="2"/></svg></div>
    <div class="abs arrow" style="left:1018px;top:208px"><svg width="16" height="32" viewBox="0 0 16 32"><path d="M2 2l12 14L2 30" fill="none" stroke="#fff" stroke-width="2"/></svg></div>
  </section>

  <div class="abs tile" style="left:156px">
    <div class="bg" role="img" aria-label="Beer bottle and glass" style="background:linear-gradient(90deg,#d8cdb8,#8a2a1c 45%,#5a1610)"></div>
    <div class="txt"><b>Beer</b><span>New Arrivals</span></div>
    <div class="tag" style="background:var(--green)">Shop Now!</div>
  </div>
  <div class="abs tile" style="left:459px">
    <div class="bg" role="img" aria-label="Man smoking a cigar" style="background:linear-gradient(90deg,#3a3a3a,#151515 55%,#0b0b0b)"></div>
    <div class="txt"><b>Cigar</b><span>Verano Reserve</span></div>
    <div class="tag" style="background:var(--navy)">Shop Now!</div>
  </div>
  <div class="abs tile" style="left:763px">
    <div class="bg" role="img" aria-label="Wine bottles with grapes" style="background:linear-gradient(90deg,#efe6d8,#b58a5c 55%,#7a4a22)"></div>
    <div class="txt"><b>Wine</b><span>Extra 25% off</span></div>
    <div class="tag" style="background:var(--green)">Shop Now!</div>
  </div>

  <div class="abs welcome-photo" role="img" aria-label="Friends sharing drinks at a table"></div>
  <section class="abs welcome">
    <div class="eyebrow">Welcome to</div>
    <h2>Copperfen Hollow</h2>
    <p>Lorem Ipsum is simply dummy text of the printing and typesetting industry. Lorem Ipsum has been the industry's standard dummy text ever since the 1500s, when an unknown printer took a galley of type and scrambled it to make a type specimen book.</p>
    <p>It has survived not only five centuries, but also the leap into electronic typesetting, remaining essentially unchanged...</p>
    <span class="btn btn-outline">Discover More</span>
  </section>

  <div class="abs products-head">
    <div><div class="eyebrow">Shop Now!</div><div class="title">Our Products</div></div>
    <div class="tabs"><span>Beer</span><span>Liquor</span><span class="on">Wine</span><span>Cigar</span><span class="btn btn-outline">View All</span></div>
  </div>

  <div class="abs card" style="left:156px"><span class="badge" style="background:var(--green)">New</span><div class="shot" role="img" aria-label="Red wine bottle"></div><h3>Ridgeline Grove<br>Zinfandel</h3><div class="price">$43.18</div><span class="btn btn-outline">Shop Now!</span></div>
  <div class="abs card raised" style="left:384px"><div class="shot" role="img" aria-label="White wine bottle"></div><h3>Ridgeline Grove<br>Zinfandel</h3><div class="price">$43.18</div><span class="btn btn-solid">Shop Now!</span></div>
  <div class="abs card" style="left:612px"><span class="badge" style="background:var(--navy)">Sale</span><div class="shot" role="img" aria-label="White wine bottle"></div><h3>Ridgeline Grove<br>Zinfandel</h3><div class="price">$43.18</div><span class="btn btn-outline">Shop Now!</span></div>
  <div class="abs card" style="left:844px"><span class="badge" style="background:var(--gold)">Specials</span><div class="shot" role="img" aria-label="Red wine bottle"></div><h3>Ridgeline Grove<br>Zinfandel</h3><div class="price">$43.18</div><span class="btn btn-outline">Shop Now!</span></div>

  <div class="abs promo" style="left:156px">
    <div class="icon"><svg width="60" height="60" viewBox="0 0 60 60"><circle cx="30" cy="30" r="28" fill="none" stroke="#fff" stroke-width="2"/><path d="M21 17c3 0 5 6 4 8l-3 2c2 5 5 8 9 10l2-3c2-1 8 1 8 4 0 3-4 6-7 5-10-3-17-10-19-20-1-3 3-6 6-6z" fill="#fff"/></svg></div>
    <div class="txt"><b>Looking To<br>Organise Party!</b><br>Need Any Help ?</div>
    <div class="tag">Call Now!</div>
  </div>
  <div class="abs promo" style="left:459px">
    <div class="icon"><svg width="44" height="54" viewBox="0 0 44 54"><rect x="2" y="2" width="40" height="50" fill="#fff"/><rect x="9" y="10" width="12" height="12" fill="#555"/><rect x="25" y="12" width="12" height="3" fill="#999"/><rect x="25" y="18" width="10" height="3" fill="#999"/><rect x="9" y="28" width="28" height="3" fill="#999"/><rect x="9" y="35" width="28" height="3" fill="#999"/><rect x="9" y="42" width="20" height="3" fill="#999"/></svg></div>
    <div class="txt"><b>We are Hiring<br>new Talented people</b><br>Send your Resume!</div>
    <div class="tag">Send Now!</div>
  </div>
  <div class="abs promo" style="left:763px">
    <div class="icon"><svg width="54" height="56" viewBox="0 0 54 56"><path d="M27 2 52 14v28L27 54 2 42V14z" fill="#fff"/><path d="M2 14l25 12 25-12M27 26v28" fill="none" stroke="#444" stroke-width="2"/></svg></div>
    <div class="txt"><b>Order Now!</b><br>Pick Up as per your<br>Convenient!</div>
    <div class="tag">Order Now!</div>
  </div>

  <h2 class="abs rev-title" style="left:156px">Patron Reviews</h2>
  <h2 class="abs rev-title" style="left:612px">Guest Reviews</h2>
  <div class="abs rev" style="left:156px;background:var(--blue);border-color:var(--blue)"><span class="q">&ldquo;</span><span class="stars">★★★★★</span> There are many variations of passages of Lorem Ipsum available, but the majority have suffered alteration in some form, by injected humour, or randomised words which don't look even slightly believable. If you are going to use...</div>
  <div class="abs rev" style="left:612px;background:var(--red);border-color:var(--red)"><span class="q">&ldquo;</span><span class="stars">★★★★☆</span> There are many variations of passages of Lorem Ipsum available, but the majority have suffered alteration in some form, by injected humour, or randomised words which don't look even slightly believable. If you are going to use...</div>
  <div class="abs author" style="left:156px"><span class="av" role="img" aria-label="Reviewer portrait"></span><div><b>Dalton Reyes</b><small>1 week ago</small></div><div class="pager"><i><svg width="8" height="10"><path d="M7 1 2 5l5 4" fill="none" stroke="#fff" stroke-width="2"/></svg></i><i><svg width="8" height="10"><path d="m1 1 5 4-5 4" fill="none" stroke="#fff" stroke-width="2"/></svg></i></div></div>
  <div class="abs author" style="left:612px"><span class="av" role="img" aria-label="Reviewer portrait"></span><div><b>Marcus Hale</b><small>2 week ago</small></div><div class="pager"><i><svg width="8" height="10"><path d="M7 1 2 5l5 4" fill="none" stroke="#fff" stroke-width="2"/></svg></i><i><svg width="8" height="10"><path d="m1 1 5 4-5 4" fill="none" stroke="#fff" stroke-width="2"/></svg></i></div></div>

  <section class="abs event" role="img" aria-label="Whisky glass with ice and a cigar">
    <h2>The Big Brands Event</h2>
    <p>Up to 50% off</p>
    <span class="btn">Explore More</span>
  </section>

  <div class="abs news-head">
    <div class="eyebrow">Recent Update</div><div class="title">Latest News</div>
    <div class="pager abs" style="right:0;top:16px"><i style="width:28px;height:28px"><svg width="8" height="10"><path d="M7 1 2 5l5 4" fill="none" stroke="#fff" stroke-width="2"/></svg></i><i style="width:28px;height:28px;background:var(--navy)"><svg width="8" height="10"><path d="m1 1 5 4-5 4" fill="none" stroke="#fff" stroke-width="2"/></svg></i></div>
  </div>
  <article class="abs news" style="left:156px"><div class="shot" role="img" aria-label="Glasses of wine with grapes" style="background:linear-gradient(135deg,#8a6a2a,#4a1a0e)"></div><div class="body"><div class="date">30-Sept.-2017</div>There are many variations of<br>passages of Lorem...<br><span class="btn btn-outline" style="margin-top:14px">Read More</span></div></article>
  <article class="abs news" style="left:612px"><div class="shot" role="img" aria-label="Man tasting red wine" style="background:linear-gradient(135deg,#6a5a4a,#2a2220)"></div><div class="body"><div class="date">30-Sept.-2017</div>There are many variations of<br>passages of Lorem...<br><span class="btn btn-solid" style="margin-top:14px">Read More</span></div></article>
  <span class="abs btn btn-outline" style="left:545px;top:2928px">View All</span>

  <section class="abs newsletter" role="img" aria-label="Wine cellar with barrels and bottles">
    <div class="eyebrow">Subscribe</div>
    <div class="title">Our Newsletter</div>
    <div class="subscribe"><span>Enter Your Email...</span><b>Subscribe</b></div>
  </section>

  <section class="abs contact">
    <div class="col"><svg width="30" height="30" viewBox="0 0 30 30"><path d="M8 3c2 0 4 5 3 7l-2 2c1 4 4 7 8 9l2-2c2-1 7 1 7 3 0 3-3 5-6 5C12 26 4 18 3 10c0-3 2-7 5-7z" fill="none" stroke="#777" stroke-width="1.5"/></svg><h4>Call Us:</h4><div class="val phone">503 - 555 - 0142</div></div>
    <div class="col"><svg width="24" height="30" viewBox="0 0 24 30"><path d="M12 29S2 17 2 11a10 10 0 0 1 20 0c0 6-10 18-10 18z" fill="none" stroke="#777" stroke-width="1.5"/><circle cx="12" cy="11" r="4" fill="none" stroke="#777" stroke-width="1.5"/></svg><h4>Head Office</h4><div class="val" style="color:#777;font-size:12px">2418 Alder Creek Rd,<br>Fenwick - OR 97301</div></div>
    <div class="col"><svg width="32" height="24" viewBox="0 0 32 24"><rect x="1" y="1" width="30" height="22" fill="none" stroke="#777" stroke-width="1.5"/><path d="m1 1 15 12L31 1" fill="none" stroke="#777" stroke-width="1.5"/></svg><h4>Email Us:</h4><div class="val">info@copperfenhollow.com</div></div>
  </section>

  <div class="abs map" role="img" aria-label="Street map showing the store locations"></div>
  <div class="abs pop"><b>Oregon</b><br>2418 Alder Creek Rd,<br>Fenwick - OR 97301<br><b>Call Us:</b><br><span class="tel">503-555-0142</span></div>

  <footer class="abs footer">
    <span>© 2017 Copperfen Hollow. All Right Reserved. | Privacy Policy</span>
    <div class="social">Get Social: <i class="dot"></i><i class="dot"></i><i class="dot"></i><i class="dot"></i><i class="dot"></i></div>
  </footer>

</div>
</body>
</html>
```